Childcare Centre Franchise Website Design

Our business is Childcare centre, and we are the franchise with 4 centres currently, we would like to have the website similar as the link below,
https://www.brambleoak.edu.au/
with the same items, functions and pages. Locations information for all centres, and have pages for each centre. Additionally, we will need a page for online enrolment.
Our logo is attached.

```html
<!DOCTYPE html>
<html lang="en">
<head>
<meta charset="utf-8">
<title>Little Sprouts Childcare &amp; Education</title>
<link href="https://fonts.googleapis.com/css2?family=Gilda+Display&family=Poppins:wght@300;400;500;600&display=swap" rel="stylesheet">
<style>
:root{
  --teal:#14a09b;
  --pink:#d63e6e;
  --cyan-bg:#dbfcfd;
  --ink:#1e1e1e;
  --muted:#8a8a8a;
  --soft:#f7f7f7;
  --line:#d9d9d9;
  --white:#ffffff;
  --social:#2b4a8a;
}
*{box-sizing:border-box;margin:0;padding:0}
html,body{width:1200px;height:5222px;overflow:hidden;background:var(--white)}
body{position:relative;font-family:"Poppins",sans-serif;color:var(--ink);font-size:13px}
.abs{position:absolute}
.serif{font-family:"Gilda Display",serif;font-weight:400}
.center{text-align:center}

.topbar{left:0;top:0;width:1200px;height:49px;background:var(--teal);color:var(--white);font-size:13px}
.topbar .promo{left:162px;top:15px}
.topbar .promo u{font-style:italic;font-weight:500}
.topbar .util{top:15px;display:flex;align-items:center;gap:8px}

.logo{left:162px;top:84px;display:flex;align-items:center;gap:10px}
.logo .mark{width:34px;height:34px;border-radius:50%;background:var(--teal)}
.logo .name{font-weight:600;color:var(--pink);font-size:15px;line-height:1.2;width:140px}
.nav{top:98px;left:396px;display:flex;gap:56px;font-size:13px;color:#777;text-align:center;line-height:1.3}
.nav .active{color:var(--ink);font-weight:500;border-bottom:2px solid var(--teal);padding-bottom:4px}

.hero-title{left:0;width:1200px;top:180px;font-size:50px;line-height:56px}
.hero-sub{left:0;width:1200px;top:304px;font-size:21px;color:#999}
.find-label{left:0;width:1200px;top:385px;font-size:14px;font-weight:500}
.search{left:371px;top:428px;width:460px;height:58px;border-radius:29px;background:var(--white);box-shadow:0 6px 22px rgba(0,0,0,.08)}
.search span{position:absolute;left:42px;top:19px;color:#aaa;font-size:13px}
.search .btn{position:absolute;right:0;top:0;width:146px;height:58px;border-radius:29px;background:var(--pink);color:var(--white);text-align:center;line-height:58px;font-size:14px}
.loc{left:0;width:1200px;top:508px;font-size:13px}
.dot{border-radius:50%}
.pill{border-radius:100px}

.trusted{left:0;width:1200px;top:978px;font-size:16px}
.brands{top:1038px;left:220px;width:760px;display:flex;justify-content:space-between;font-size:30px;font-weight:600;color:#c8c8c8}

.feat-circle{width:166px;height:166px;border-radius:50%;background:var(--white);border:2px solid #d6ecea;box-shadow:0 10px 30px rgba(0,0,0,.07)}
.feat-circle i{position:absolute;left:55px;top:55px;width:56px;height:56px;border-radius:12px;display:block}
.feat-title{font-size:27px;color:var(--teal)}
.feat-text{font-size:13px;line-height:19px;text-align:center}
.feat-link{font-size:13px;color:var(--teal);text-decoration:underline;font-weight:500;text-align:center}

.learning{left:0;top:1692px;width:1200px;height:670px;background:var(--cyan-bg)}
.learn-card{top:1918px;width:211px;height:243px;background:var(--white);border:2px solid #c9c9c9;border-radius:10px;box-shadow:0 8px 20px rgba(0,0,0,.12)}
.learn-card .ph{position:absolute;left:10px;top:10px;width:187px;height:140px;border-radius:4px}
.learn-card p{position:absolute;left:0;width:207px;top:168px;text-align:center;color:var(--teal);font-family:"Gilda Display",serif;font-size:21px;line-height:25px}
.btn-pink{background:var(--pink);color:var(--white);border-radius:40px;text-align:center;font-size:14px}

.news-card{top:2621px;width:284px;height:434px;background:var(--soft)}
.news-card .ph{height:199px;width:100%}
.news-card .body{padding:26px 24px 0}
.news-card .date{font-size:12px}
.news-card h3{font-size:16px;font-weight:600;line-height:23px;margin-top:10px}
.news-card p{font-size:12px;line-height:18px;margin-top:12px;color:#333}
.news-card .more{display:block;margin-top:20px;color:var(--teal);font-size:13px;font-weight:500;text-decoration:underline}

.village{left:0;top:3178px;width:1200px;height:759px;background:#f8f8f8}
.v-card{width:282px;height:123px;background:var(--white);border-radius:12px}
.v-card .ph{position:absolute;left:16px;top:19px;width:78px;height:85px;border-radius:8px}
.v-card .t{position:absolute;left:108px;top:32px;font-family:"Gilda Display",serif;font-size:16px;line-height:20px}
.v-card .s{position:absolute;left:108px;top:76px;font-size:11px;color:var(--teal)}

.field{border-bottom:1px solid var(--line);font-size:12px;color:#777}
.banner{left:162px;top:4654px;width:878px;height:195px;background:var(--teal);color:var(--white);text-align:center;font-family:"Gilda Display",serif;font-size:29px;line-height:38px;padding-top:40px}
.footer-h{font-size:14px;font-weight:500}
.footer-list{font-size:12px;line-height:24px}
</style>
</head>
<body>

<div class="abs topbar">
  <div class="abs promo">Calculate Your Child Care Subsidy. <u>LEARN MORE</u></div>
  <div class="abs util" style="left:785px">
    <svg width="14" height="16" viewBox="0 0 14 16"><path d="M7 0a6 6 0 0 0-6 6c0 4.5 6 10 6 10s6-5.5 6-10a6 6 0 0 0-6-6zm0 8.5A2.5 2.5 0 1 1 7 3.5a2.5 2.5 0 0 1 0 5z" fill="#fff"/></svg>
    Find Center</div>
  <div class="abs util" style="left:930px">
    <svg width="15" height="15" viewBox="0 0 24 24"><path d="M6.6 10.8a15 15 0 0 0 6.6 6.6l2.2-2.2c.3-.3.7-.4 1-.2 1.1.4 2.3.6 3.6.6.6 0 1 .4 1 1V20c0 .6-.4 1-1 1A17 17 0 0 1 3 4c0-.6.4-1 1-1h3.5c.6 0 1 .4 1 1 0 1.3.2 2.5.6 3.6.1.3 0 .7-.2 1z" fill="#fff"/></svg>
    1300 555 014</div>
</div>

<div class="abs logo"><span class="mark"></span><span class="name">LITTLE SPROUTS</span></div>
<nav class="abs nav">
  <div>Childcare<br>&amp; Education</div>
  <div class="active">Childcare<br>Centres</div>
  <div>Childcare<br>Subsidy</div>
  <div>News<br>&amp; Advice</div>
  <div>About<br>Us</div>
  <div style="padding-top:9px">Careers</div>
</nav>

<h1 class="abs serif center hero-title">Creating a World Of<br>Wonder And Imagination.</h1>
<div class="abs serif center hero-sub">Be Creative. Be Brave. Be Curious</div>
<div class="abs center find-label">FIND YOUR CENTRE TO ENROL</div>
<div class="abs search"><span>Enter Postcode or Suburb</span><div class="btn">Search</div></div>
<div class="abs center loc">Or Use Your Current Location</div>

<div class="abs dot" style="left:246px;top:423px;width:24px;height:24px;background:var(--teal)"></div>
<div class="abs dot" style="left:82px;top:541px;width:16px;height:16px;background:var(--pink)"></div>
<div class="abs dot" style="left:555px;top:584px;width:16px;height:16px;background:var(--pink)"></div>
<div class="abs dot" style="left:956px;top:496px;width:16px;height:16px;background:var(--pink)"></div>
<div class="abs dot" style="left:1082px;top:862px;width:16px;height:16px;background:var(--pink)"></div>
<div class="abs dot" style="left:295px;top:902px;width:24px;height:24px;background:var(--teal)"></div>
<div class="abs dot" style="left:780px;top:914px;width:24px;height:24px;background:var(--teal)"></div>

<div class="abs pill" role="img" aria-label="Two young children in knitted beanies hugging on a yellow background" style="left:162px;top:566px;width:195px;height:294px;background:linear-gradient(160deg,#e9a13a,#d08a34)"></div>
<div class="abs pill" role="img" aria-label="Girl covering her ears on a pink background" style="left:389px;top:620px;width:197px;height:292px;background:linear-gradient(160deg,#f4b1b9,#e89aa4)"></div>
<div class="abs pill" role="img" aria-label="Excited boy wearing headphones in a red shirt" style="left:616px;top:566px;width:197px;height:294px;background:linear-gradient(160deg,#c9c9c9,#b83a35)"></div>
<div class="abs pill" role="img" aria-label="Smiling girl holding a toy globe" style="left:843px;top:620px;width:199px;height:292px;background:linear-gradient(160deg,#eeeeee,#cfd6dc)"></div>

<div class="abs center trusted">Trusted By Many Renowned Companies.</div>
<div class="abs brands"><span>Northwind</span><span>Apexa</span><span>Corvo</span><span>Lumen</span><span>Halden</span></div>

<svg class="abs" style="left:0;top:1180px" width="1200" height="200" viewBox="0 0 1200 200">
  <path d="M0 90 C80 120 150 140 215 150 M377 140 C430 120 470 80 515 68 M676 50 C730 60 780 90 822 102 M986 150 C1060 145 1140 110 1200 62" fill="none" stroke="#14a09b" stroke-width="2" stroke-dasharray="6 6"/>
</svg>

<div class="abs feat-circle" style="left:213px;top:1251px"><i role="img" aria-label="Envelope with coins icon" style="background:#f3c14d"></i></div>
<div class="abs feat-circle" style="left:511px;top:1157px"><i role="img" aria-label="Shield and sword icon" style="background:#e8a240"></i></div>
<div class="abs feat-circle" style="left:821px;top:1228px"><i role="img" aria-label="Heart with medical crosses icon" style="background:#e55a7a"></i></div>

<div class="abs serif center feat-title" style="left:140px;width:310px;top:1452px">Child Care Subsidy</div>
<div class="abs feat-text" style="left:160px;width:270px;top:1498px">Lorem Ipsum is simply dummy text of the printing and typesetting industry. Lorem Ipsum has been the industry's standard dummy text ever since the 1500s,</div>
<div class="abs feat-link" style="left:160px;width:270px;top:1590px">Calculate Your CCS</div>

<div class="abs serif center feat-title" style="left:430px;width:330px;top:1352px">Why Wattle Grove?</div>
<div class="abs feat-text" style="left:458px;width:274px;top:1399px">Lorem Ipsum is simply dummy text of the printing and typesetting industry. Lorem Ipsum has been the industry's standard dummy text ever since the 1500s,</div>
<div class="abs feat-link" style="left:458px;width:274px;top:1496px">Learn More</div>

<div class="abs serif center feat-title" style="left:750px;width:310px;top:1435px">Health &amp; Wellbeing</div>
<div class="abs feat-text" style="left:768px;width:274px;top:1483px">Lorem Ipsum is simply dummy text of the printing and typesetting industry. Lorem Ipsum has been the industry's standard dummy text ever since the 1500s,</div>
<div class="abs feat-link" style="left:768px;width:274px;top:1582px">Learn More</div>

<div class="abs learning"></div>
<h2 class="abs serif center" style="left:0;width:1200px;top:1752px;font-size:46px;line-height:60px">Learning. Confidence.<br>Curiosity.</h2>
<div class="abs learn-card" style="left:162px"><div class="ph" role="img" aria-label="Happy children playing together in a classroom" style="background:linear-gradient(160deg,#d9b59a,#8c6a55)"></div><p>High-Quality<br>Curriculum</p></div>
<div class="abs learn-card" style="left:385px"><div class="ph" role="img" aria-label="Girl showing hands covered in colourful paint" style="background:linear-gradient(160deg,#f1e4b0,#e9a45c)"></div><p>Exciting<br>Environments</p></div>
<div class="abs learn-card" style="left:607px"><div class="ph" role="img" aria-label="Child enjoying healthy vegetables at a table" style="background:linear-gradient(160deg,#e8ece8,#7fae5a)"></div><p>Wellbeing &amp;<br>Nutrition</p></div>
<div class="abs learn-card" style="left:829px"><div class="ph" role="img" aria-label="Group of smiling children with a ball" style="background:linear-gradient(160deg,#c8d3c0,#d9a15a)"></div><p>Community<br>Connections</p></div>
<div class="abs btn-pink" style="left:468px;top:2232px;width:264px;height:59px;line-height:59px">Discover Our Approach</div>

<h2 class="abs serif center" style="left:0;width:1200px;top:2436px;font-size:46px;line-height:60px">Latest News &amp; Advice From<br>Our Team Of Experts</h2>
<div class="abs news-card" style="left:162px"><div class="ph" role="img" aria-label="Two boys playing football on a path" style="background:linear-gradient(160deg,#a9c98a,#6d7a84)"></div><div class="body"><div class="date">20 May 2023</div><h3>10 signs your child might be ready for school.</h3><p>Each year around this time, our Centres begin to have conversations and meetings with parents who are still deciding whether to send......</p><span class="more">Red More</span></div></div>
<div class="abs news-card" style="left:458px"><div class="ph" role="img" aria-label="Children playing tug of war outdoors" style="background:linear-gradient(160deg,#b7c9a4,#8a7360)"></div><div class="body"><div class="date">20 May 2023</div><h3>Risky Business: Appropriate Risks During Play.</h3><p>Taking risks is an important part of life. It's also important in the development of children. By taking appropriate risks......</p><span class="more">Red More</span></div></div>
<div class="abs news-card" style="left:756px"><div class="ph" role="img" aria-label="Children gardening and playing in a park" style="background:linear-gradient(160deg,#8fb36e,#5b4a3c)"></div><div class="body"><div class="date">20 May 2023</div><h3>Meet Maya - Centre Manager at Wattle Grove Park.</h3><p>Maya, Centre Manager of our Croydon Park Centre, is an incredible leader and a valued member of our Wattle Grove......</p><span class="more">Red More</span></div></div>

<div class="abs village"></div>
<h2 class="abs serif center" style="left:0;width:1200px;top:3236px;font-size:46px">Find Your Village</h2>
<div class="abs v-card" style="left:162px;top:3355px"><div class="ph" role="img" aria-label="Children playing on a playground" style="background:linear-gradient(160deg,#9cb884,#5d6f8a)"></div><div class="t">Little Sprouts<br>Childcare &amp; Education</div><div class="s">Bentleigh</div></div>
<div class="abs v-card" style="left:459px;top:3355px"><div class="ph" role="img" aria-label="Child on a swing" style="background:linear-gradient(160deg,#a9c78a,#d8b36a)"></div><div class="t">Little Sprouts<br>Childcare &amp; Education</div><div class="s">Bentleigh</div></div>
<div class="abs v-card" style="left:756px;top:3355px"><div class="ph" role="img" aria-label="Children doing crafts" style="background:linear-gradient(160deg,#e0b04a,#6a7a3e)"></div><div class="t">Little Sprouts<br>Childcare &amp; Education</div><div class="s">Bentleigh</div></div>
<div class="abs v-card" style="left:162px;top:3495px"><div class="ph" role="img" aria-label="Childcare centre building" style="background:linear-gradient(160deg,#8fb7d8,#b98a6a)"></div><div class="t">Little Sprouts<br>Childcare &amp; Education</div><div class="s">Bentleigh</div></div>
<div class="abs v-card" style="left:459px;top:3495px"><div class="ph" role="img" aria-label="Children playing on grass" style="background:linear-gradient(160deg,#a6c57c,#c9a46e)"></div><div class="t">Little Sprouts<br>Childcare &amp; Education</div><div class="s">Bentleigh</div></div>
<div class="abs v-card" style="left:756px;top:3495px"><div class="ph" role="img" aria-label="Children with colourful toys" style="background:linear-gradient(160deg,#5d8fc7,#d9603e)"></div><div class="t">Little Sprouts<br>Childcare &amp; Education</div><div class="s">Bentleigh</div></div>
<div class="abs v-card" style="left:162px;top:3635px"><div class="ph" role="img" aria-label="Centre playroom" style="background:linear-gradient(160deg,#c9b7a6,#8a6d5c)"></div><div class="t">Little Sprouts<br>Childcare &amp; Education</div><div class="s">Bentleigh</div></div>
<div class="abs v-card" style="left:459px;top:3635px"><div class="ph" role="img" aria-label="Child playing outdoors" style="background:linear-gradient(160deg,#b3c98f,#7a6a55)"></div><div class="t">Little Sprouts<br>Childcare &amp; Education</div><div class="s">Bentleigh</div></div>
<div class="abs v-card" style="left:756px;top:3635px"><div class="ph" role="img" aria-label="Children painting together" style="background:linear-gradient(160deg,#d9a58c,#4e6b9a)"></div><div class="t">Little Sprouts<br>Childcare &amp; Education</div><div class="s">Bentleigh</div></div>
<div class="abs btn-pink" style="left:203px;top:3811px;width:208px;height:59px;line-height:59px">View All Centers</div>
<div class="abs btn-pink" style="left:497px;top:3811px;width:208px;height:59px;line-height:59px">View All Centers</div>
<div class="abs btn-pink" style="left:790px;top:3811px;width:208px;height:59px;line-height:59px">View All Centers</div>

<h2 class="abs serif" style="left:162px;top:4012px;font-size:46px">Online Enrolment</h2>
<div class="abs" style="left:162px;top:4075px;font-size:14px;color:#999">Lorem ipsum dolor sit amet, consectetur.</div>
<div class="abs field" style="left:162px;top:4140px;width:444px;height:46px;padding:8px 16px">Your Full Name</div>
<div class="abs field" style="left:162px;top:4202px;width:178px;height:46px;padding:8px 16px">Email</div>
<div class="abs field" style="left:400px;top:4202px;width:206px;height:46px;padding:8px 16px">Phone Number</div>
<div class="abs field" style="left:162px;top:4264px;width:178px;height:46px;padding:8px 16px">Date Of Birth</div>
<div class="abs field" style="left:400px;top:4264px;width:206px;height:46px;padding:8px 16px">Zip Code</div>
<div class="abs field" style="left:162px;top:4326px;width:444px;height:122px;padding:8px 16px">Query</div>
<div class="abs btn-pink" style="left:162px;top:4472px;width:209px;height:59px;line-height:59px">Enroll Now</div>
<div class="abs" role="img" aria-label="Girl in a teal top using a laptop" style="left:667px;top:4014px;width:395px;height:537px;background:linear-gradient(160deg,#eeeeee,#b9c6c4 60%,#4fb9b0)"></div>

<div class="abs" style="left:0;top:4750px;width:1200px;height:472px;background:linear-gradient(180deg,#f4f4f4,#ffffff 55%)"></div>
<div class="abs banner">Childcare is More than a Career at Wattle Grove<br>Children are the heart of our Centres<br>&amp; our people are the soul.</div>

<div class="abs logo" style="top:4900px"><span class="mark"></span><span class="name">LITTLE SPROUTS</span></div>
<div class="abs" style="left:162px;top:4974px;font-size:12px;font-weight:600">Little Sprouts Childcare &amp; Education.</div>
<div class="abs" style="left:162px;top:4996px;width:360px;font-size:12px;line-height:24px">Lorem Ipsum is simply dummy text of the printing and typesetting industry. Lorem Ipsum has been the industry's standard dummy text ever since the 1500s,</div>

<div class="abs footer-h" style="left:583px;top:4920px">QUICK LINKS</div>
<div class="abs footer-list" style="left:583px;top:4950px">Childcare &amp; Education<br>Childcare Centres<br>Childcare Subsidy<br>News &amp; Advice<br>Careers<br>About Us</div>

<div class="abs footer-h" style="left:783px;top:4920px">FOLLOW US</div>
<div class="abs" style="left:783px;top:4950px;font-size:12px">Subscribe Our Newsletter.</div>
<div class="abs" style="left:783px;top:4982px;display:flex;gap:6px">
  <span class="dot" style="width:20px;height:20px;background:var(--social);display:block"></span>
  <span class="dot" style="width:20px;height:20px;background:var(--social);display:block"></span>
  <span class="dot" style="width:20px;height:20px;background:var(--social);display:block"></span>
  <span class="dot" style="width:20px;height:20px;background:var(--social);display:block"></span>
</div>
<div class="abs field" style="left:783px;top:5028px;width:255px;height:40px;padding:8px 20px;color:#333">Enter Email Address.</div>
<svg class="abs" style="left:1000px;top:5038px" width="18" height="18" viewBox="0 0 24 24"><path d="M2 21l21-9L2 3v7l15 2-15 2z" fill="#14a09b"/></svg>

<div class="abs" style="left:150px;top:5188px;font-size:12px">Copyright @ 2023. <b style="font-weight:600">Little Sprouts Childcare &amp; Education.</b> All Right Reserved.</div>
<div class="abs" style="left:815px;top:5188px;font-size:12px">Terms &amp; Conditions | Privacy Policy</div>

</body>
</html>
```